Flier for digital rights event targetting TMVA trade negotiators

We need a design for an event that my organization (a nonprofit) is hosting with academic experts, to address government negotiators who are taking part in the 19th round of negotiations of the Coastal Integrated Commerce Accord (TMVA). Unfortunately we don't have the exact details yet such as who the speakers are, what date the meeting is, or even what location it is, other than that it will be in Hyderabad, India. So you will need to make a design with placeholder values that we can swap out later. Here is some information about TMVA: https://en.examplepedia.org/wiki/Coastal_Integrated_Commerce_Accord. The event will be called: "An Expert Roundtable on Electronic Commerce and TMVA". I'm attaching some similar fliers for previous events.

Target Market(s)

Government trade ministries

Industry/Entity Type

Trade

Font styles to use
Serif
Sans Serif

Colors

Designer to choose colors to be used in the design.

Requirements
Must have
• Space for organizer logos, including LKB logo from https://www.lkbnet.org/press/logos
Nice to have
• Space for headshots of speakers (even though we haven't finalized who they are yet)
Should not have
• Cheesy stock graphics

```html
<!DOCTYPE html>
<html lang="en">
<head>
<meta charset="utf-8">
<title>An Expert Roundtable on Electronic Commerce and TMVA</title>
<link rel="stylesheet" href="https://fonts.googleapis.com/css2?family=Roboto+Condensed:wght@400;700&family=Open+Sans:wght@400;600;700&display=swap">
<style>
  :root {
    --red: #e3262c;
    --ink: #231f20;
    --body-text: #3a3a3a;
    --grey-top: #d4d5d6;
    --paper: #ffffff;
    --night: #1d3566;
    --glow: #e39a4a;
  }
  html, body {
    margin: 0;
    padding: 0;
    width: 873px;
    height: 1200px;
    overflow: hidden;
    background: var(--paper);
  }
  .flier {
    position: relative;
    width: 873px;
    height: 1200px;
    overflow: hidden;
    background: linear-gradient(180deg, var(--grey-top) 0%, #eeeeef 18%, var(--paper) 30%, var(--paper) 100%);
    font-family: "Open Sans", sans-serif;
  }
  .brand {
    position: absolute;
    top: 52px;
    left: 0;
    width: 873px;
    display: flex;
    justify-content: center;
    align-items: center;
    gap: 18px;
  }
  .brand-mark {
    width: 58px;
    height: 58px;
    border-radius: 50%;
    background: var(--red);
  }
  .brand-name {
    font-family: "Roboto Condensed", sans-serif;
    font-weight: 400;
    font-size: 29px;
    letter-spacing: 1.5px;
    color: var(--ink);
  }
  .title {
    position: absolute;
    top: 112px;
    left: 0;
    width: 873px;
    margin: 0;
    text-align: center;
    font-family: "Roboto Condensed", sans-serif;
    font-weight: 700;
    font-size: 46px;
    line-height: 50px;
    color: var(--red);
  }
  .hero-art {
    position: absolute;
    top: 0;
    left: 0;
  }
  .venue {
    position: absolute;
    top: 750px;
    left: 0;
    width: 873px;
    margin: 0;
    text-align: center;
    font-family: "Roboto Condensed", sans-serif;
    font-weight: 700;
    font-size: 33px;
    color: var(--ink);
  }
  .venue .label { color: var(--red); }
  .date-box {
    position: absolute;
    top: 802px;
    left: 178px;
    width: 670px;
    height: 48px;
    box-sizing: border-box;
    border: 1.5px solid var(--red);
    display: flex;
    align-items: center;
    justify-content: center;
    font-family: "Roboto Condensed", sans-serif;
    font-weight: 700;
    font-size: 34px;
    color: var(--ink);
    transform: translateX(-78px);
  }
  .date-box .day { color: var(--red); margin-right: 9px; }
  .speaker {
    position: absolute;
    left: 0;
    width: 873px;
    height: 130px;
  }
  .speaker-one { top: 875px; }
  .speaker-two { top: 1005px; }
  .headshot {
    position: absolute;
    width: 108px;
    height: 108px;
    border-radius: 50%;
    border: 2px solid var(--red);
    box-sizing: border-box;
    background: radial-gradient(circle at 50% 40%, #9aa0a8 0%, #5b5f66 60%, #2f3136 100%);
  }
  .speaker-one .headshot { left: 55px; top: 6px; }
  .speaker-two .headshot { left: 50px; top: 6px; }
  .quote-open, .quote-close {
    position: absolute;
    font-family: "Open Sans", sans-serif;
    font-weight: 700;
    font-size: 64px;
    line-height: 1;
    color: var(--red);
  }
  .quote-open { left: 274px; top: 8px; }
  .quote-close { left: 864px; top: 90px; transform: translateX(-70px); }
  .speaker-blurb {
    position: absolute;
    left: 276px;
    top: 42px;
    width: 512px;
    margin: 0;
    font-size: 12.4px;
    line-height: 19px;
    color: var(--body-text);
    text-align: justify;
  }
  .contact {
    position: absolute;
    top: 1140px;
    left: 0;
    width: 873px;
    display: flex;
    justify-content: center;
    align-items: center;
    gap: 18px;
    font-family: "Roboto Condensed", sans-serif;
    font-weight: 700;
  }
  .call {
    font-size: 31px;
    color: var(--ink);
  }
  .call .number { color: var(--red); }
  .divider {
    width: 1px;
    height: 26px;
    background: #b5b5b5;
  }
  .web {
    font-family: "Open Sans", sans-serif;
    font-size: 22px;
    color: var(--red);
  }
  .web .domain { color: var(--ink); }
  .footer-bar {
    position: absolute;
    bottom: 0;
    left: 0;
    width: 873px;
    height: 9px;
    display: flex;
  }
  .footer-bar .red-part { width: 627px; background: var(--red); }
  .footer-bar .dark-part { flex: 1; background: var(--ink); }
</style>
</head>
<body>
<main class="flier">

  <header class="brand">
    <span class="brand-mark"></span>
    <span class="brand-name">LANTERN KEY BUREAU</span>
  </header>

  <h1 class="title">An Expert Roundtable on<br>Electronic Commerce and TMVA</h1>

  <svg class="hero-art" width="873" height="1200" viewBox="0 0 873 1200">
    <defs>
      <linearGradient id="cityGlow" x1="0" y1="0" x2="0" y2="1">
        <stop offset="0" stop-color="#1a2c57"/>
        <stop offset="0.55" stop-color="#2b3f6e"/>
        <stop offset="0.8" stop-color="#8a6a4a"/>
        <stop offset="1" stop-color="#e39a4a"/>
      </linearGradient>
    </defs>
    <path class="swoosh-dark" d="M0,328 Q436,176 873,284 L873,300 Q436,214 0,342 Z" fill="#231f20"/>
    <path class="hero-photo" role="img" aria-label="Evening photograph of a historic Hyderabad monument with busy street lights"
          d="M0,350 Q436,230 873,304 L873,590 Q420,807 0,620 Z" fill="url(#cityGlow)"/>
    <path class="swoosh-red" d="M0,620 Q420,807 873,590 L873,605 Q430,833 0,690 Z" fill="#e3262c"/>
  </svg>

  <p class="venue"><span class="label">Venue:</span> Harborview Hyderabad Convention Centre.</p>

  <div class="date-box"><span class="day">FRIDAY, 21ST JULY</span> FROM 5:30PM</div>

  <section class="speaker speaker-one">
    <div class="headshot" role="img" aria-label="Speaker headshot"></div>
    <span class="quote-open">&ldquo;</span>
    <p class="speaker-blurb">Lorem ipsum dolor sit amet, consectetur adipiscing elit. Vivamus dignissim massa in porta porttitor. Praesent vitae risus ut nibh vulputate efficitur non ut lacus. Aenean tempus, risus et aliquet vehicula, felis ligula malesuada leo, vitae porttitor diam tortor vitae quam. Morbi at feugiat turpis. Donec in eros vel sapien blandit molestie quis eget justo. Ut dignissim non elit vel tempor.</p>
    <span class="quote-close">&rdquo;</span>
  </section>

  <section class="speaker speaker-two">
    <div class="headshot" role="img" aria-label="Speaker headshot"></div>
    <span class="quote-open">&ldquo;</span>
    <p class="speaker-blurb">Lorem ipsum dolor sit amet, consectetur adipiscing elit. Vivamus dignissim massa in porta porttitor. Praesent vitae risus ut nibh vulputate efficitur non ut lacus. Aenean tempus, risus et aliquet vehicula, felis ligula malesuada leo, vitae porttitor diam tortor vitae quam. Morbi at feugiat turpis. Donec in eros vel sapien blandit molestie quis eget justo. Ut dignissim non elit vel tempor.</p>
    <span class="quote-close">&rdquo;</span>
  </section>

  <footer class="contact">
    <span class="call">CALL US:<span class="number">1234 123 456</span></span>
    <span class="divider"></span>
    <span class="web">www.<span class="domain">website</span>.com</span>
  </footer>

  <div class="footer-bar"><span class="red-part"></span><span class="dark-part"></span></div>

</main>
</body>
</html>
```